Web Site Design for a Finance (lending) Company

We are opening a new subsidiary that focuses on lending money in the real estate industry. We need a web site designed to represent the business.

The business is lending money to real estate investors. A typical client/borrower will be looking to borrow money to buy a house, renovate it and then sell it at a profit, all within 12 months or less.

Company name is Varlo Finance. Our logo is attached.

Attached is a general outline for the web site. We're working on writing more text for each page but this should give you enough to get started with some ideas.

Competitor web site that I like a lot (as an example): https://brixhallfunding.example/. Many of the general items on this site match what we will need (description of loan programs, FAQ)

Target Market(s)

Real estate investors (generally individuals or small companies with just a few people) who are buying homes, renovating them and then selling them at a profit.

Industry/Entity Type

Finance

Coding

Coded - Design and coding required

Number of Pages Required

5+ page

Colors

Designer to choose colors to be used in the design.

Requirements
Must have
• Minimalist design. Clean lines without too much clutter. Some stock photography is ok but the photos should not be distracting. They should almost fade in to the background so that user can focus on the key information about what our company does instead. We are a finance company, not a design company, so the information about our products will be more interesting to site visitors than the art.
• Some minimalist examples from Mosaiko:
• https://www.mosaiko.example/explore/minimalist-web-design/
Nice to have
• If you search in searchly for "hard money lenders" you will find many examples of web sites from our competition. I have provided a link above to competitor web site that I like a lot.
• I have attached our logo in EPS format. Logo is green. Web site doesn't have to be green but it should be of a color that will work well with the logo.

```html
<!DOCTYPE html>
<html lang="en">
<head>
<meta charset="utf-8">
<title>Varlo Finance</title>
<link href="https://fonts.googleapis.com/css2?family=DM+Sans:wght@400;500;700&display=swap" rel="stylesheet">
<style>
:root{
  --green:#5a9c3a;
  --ink:#1e1e1e;
  --muted:#555;
  --soft:#9a9a9a;
  --rule:#dcdcdc;
  --panel:#f3f2ee;
  --stage:#f5f4f0;
  --btn:#b4b1a4;
}
*{margin:0;padding:0;box-sizing:border-box}
html,body{width:746px;height:1200px;overflow:hidden;background:var(--stage);font-family:"DM Sans",sans-serif;color:var(--ink)}
.page{position:absolute;left:84px;top:0;width:578px;height:1200px;background:#fff}
.abs{position:absolute}
.brand{font-weight:700;color:var(--green);font-size:10px;letter-spacing:.2px}
.nav-col{position:absolute;top:26px;width:74px;border-top:1px solid var(--rule);padding-top:5px;font-size:5px;line-height:7px;color:var(--muted)}
.nav-col h4,.foot-col h4{font-size:6.5px;font-weight:500;color:var(--ink);margin-bottom:3px}
.photo{position:absolute}
.hero-title{font-size:16px;line-height:19px;font-weight:400;width:200px}
.hero-text{font-size:5.8px;line-height:8px;color:var(--muted);width:150px}
.label{font-size:5.8px}
.select{border:1px solid #cfcfcf;background:#f8f8f6;font-size:6px;color:var(--muted);padding:0 8px;display:flex;align-items:center;justify-content:space-between}
.dot{width:4px;height:4px;border-radius:50%;background:var(--green)}
.why{left:44px;top:347px;width:490px;height:230px;background:var(--panel);text-align:center}
.why h2{position:absolute;top:40px;width:100%;font-size:12px;font-weight:400}
.why p.lead{position:absolute;top:58px;left:125px;width:240px;font-size:5.8px;line-height:8px;color:var(--muted)}
.feature{position:absolute;top:94px;width:96px;font-size:5.5px;line-height:7px;color:var(--muted)}
.feature svg{display:block;margin:0 auto 10px}
.feature h3{font-size:6px;font-weight:500;color:var(--ink);margin-bottom:3px}
.btn{position:absolute;left:221px;top:188px;width:49px;height:19px;background:var(--btn);color:#fff;font-size:5.5px;line-height:19px;border-radius:2px}
.sec-head{position:absolute;border-top:1px solid var(--rule);display:flex;justify-content:space-between;padding-top:7px;font-size:7px;font-weight:500}
.link{font-size:5px;font-weight:400;border-bottom:1px solid var(--green);padding-bottom:1px;height:max-content}
.feature-card{left:44px;top:635px;width:299px;height:149px;background:linear-gradient(120deg,#6e6a62,#a39a8e 55%,#8c99a5)}
.feature-card h3{position:absolute;left:20px;top:82px;color:#fff;font-size:13px;line-height:17px;font-weight:400;width:200px}
.feature-card .link{position:absolute;left:20px;top:128px;color:#fff}
.case-title{font-size:9px;line-height:12px;width:160px}
.green-link{color:var(--green)}
.news{position:absolute;top:852px;width:157px;height:106px}
.news h4{position:absolute;left:0;top:8px;width:86px;font-size:6.8px;line-height:8.5px;font-weight:500;border-top:1px solid var(--rule);padding-top:0}
.news .rule{position:absolute;left:0;top:0;width:86px;border-top:1px solid var(--rule)}
.news .rule2{position:absolute;left:0;top:63px;width:86px;border-top:1px solid var(--rule)}
.news p{position:absolute;left:0;top:66px;width:86px;font-size:5px;line-height:6.5px;color:var(--muted)}
.news .link{position:absolute;left:0;top:98px}
.news .pic{position:absolute;right:0;top:0;width:66px;height:100px}
.partners{position:absolute;left:44px;top:1036px;width:490px;display:flex;justify-content:space-between;align-items:center;font-size:8px;font-weight:500;color:#8a8a8a}
.foot-col{position:absolute;top:1094px;font-size:5px;line-height:7px;color:var(--muted);padding-top:10px}
.footline{left:44px;top:1094px;width:490px;border-top:1px solid var(--rule)}
.legal{font-size:4.5px;color:var(--muted)}
</style>
</head>
<body>
<div class="page">
  <div class="abs brand" style="left:44px;top:24px">Varlo Finance</div>

  <nav>
    <div class="nav-col" style="left:218px"><h4>About</h4>Company<br>People</div>
    <div class="nav-col" style="left:301px"><h4>Loans</h4>Fix and Flip<br>Commercial Hard Money</div>
    <div class="nav-col" style="left:384px"><h4>Resources</h4>Blog<br>Industry News<br>Vallue Add Services<br>Testimonials</div>
    <div class="nav-col" style="left:467px"><h4>Contact</h4><span style="color:var(--soft)">info@varlofinance.example</span><br>1 (888) 555 0147<br>48 Alder Row, Fernbrook,<br>PA, 32904</div>
  </nav>

  <section class="hero">
    <div class="abs" style="left:302px;top:122px;width:8px;height:191px;background:var(--green)"></div>
    <div class="photo" role="img" aria-label="Smiling young woman seated in a bright office" style="left:44px;top:78px;width:266px;height:202px;background:linear-gradient(110deg,#3d3a35,#c9b9a7 45%,#e6ddd2 70%,#a9b2a6)"></div>
    <h1 class="abs hero-title" style="left:335px;top:160px">Local real estate experts lending to local real estate investors</h1>
    <p class="abs hero-text" style="left:335px;top:227px">Join an established pool of experienced investors available for your real estate investment needs, and collaborate with partners with a wide network who offers value added services.</p>
    <div class="abs label" style="left:335px;top:281px">I am interested in</div>
    <div class="abs select" style="left:334px;top:293px;width:142px;height:20px">Fix and Flip Loans<span class="dot"></span></div>
  </section>

  <section class="abs why">
    <h2>Why borrow from Varlo finance?</h2>
    <p class="lead">Borrow from an established pool of experienced investors available for your real estate investment needs, and collaborate with partners with a wide network who offers value added services</p>
    <div class="feature" style="left:16px;text-align:left">
      <svg width="26" height="24" viewBox="0 0 26 24" fill="none" stroke="#5a9c3a" stroke-width="1"><rect x="11" y="1" width="4" height="4"/><rect x="3" y="9" width="4" height="4"/><rect x="19" y="9" width="4" height="4"/><rect x="3" y="18" width="4" height="4"/><rect x="19" y="18" width="4" height="4"/><path d="M13 5v5M11 12l2-2 2 2M10 20h6"/></svg>
      <h3>Profesionnal experts</h3>A team attentive to your expectations to provide you with added value</div>
    <div class="feature" style="left:137px">
      <svg width="20" height="22" viewBox="0 0 20 22" fill="none" stroke="#5a9c3a" stroke-width="1"><path d="M3 1h10l3 3v12H3z"/><path d="M6 6h7M6 9h7M6 12h5"/><circle cx="15" cy="17" r="4" fill="#5a9c3a"/><path d="M13 17l1.5 1.5 2.5-3" stroke="#fff"/></svg>
      <h3>Selective &amp; Fast approvals</h3>Our selection process is designed to be as quick and straightforward as possible</div>
    <div class="feature" style="left:259px">
      <svg width="26" height="22" viewBox="0 0 26 22" fill="none" stroke="#5a9c3a" stroke-width="1"><rect x="6" y="1" width="18" height="11"/><rect x="2" y="7" width="18" height="11"/><circle cx="11" cy="12.5" r="2.5"/><path d="M4 21h18"/></svg>
      <h3>Competitive rates &amp; fees</h3>We offer loans with low interest rates and term options to fit your personal needs</div>
    <div class="feature" style="left:380px">
      <svg width="26" height="22" viewBox="0 0 26 22" fill="none" stroke="#5a9c3a" stroke-width="1"><path d="M2 8l6-6 5 4 5-4 6 6-9 10z"/><path d="M8 11l4 4M11 9l4 4"/></svg>
      <h3>Sustained partnership</h3>Customers will benefit from a sustained partnership, and a focus on results measurement and efficiency</div>
    <div class="btn">Details</div>
  </section>

  <div class="sec-head" style="left:44px;top:610px;width:299px">People<span class="link">Company</span></div>
  <article class="abs feature-card" role="img" aria-label="Young couple reviewing loan documents with an advisor">
    <h3>5 good reasons to apply for a loan with Varlo Finance</h3>
    <span class="link" style="font-size:5px">Discover</span>
  </article>

  <div class="sec-head" style="left:376px;top:610px;width:158px">Cases studies<span class="link">Borrowers</span></div>
  <div class="photo" role="img" aria-label="Large tudor style house under a blue sky" style="left:376px;top:635px;width:158px;height:106px;background:linear-gradient(180deg,#6f9cc4,#a9c6de 45%,#7a5a45 62%,#5e8a3c 85%)"></div>
  <h3 class="abs case-title" style="left:376px;top:749px;font-weight:400">$700K Trust Deed Investment Closed on Downtown in Melbourne</h3>
  <span class="abs link green-link" style="left:376px;top:776px">Discover</span>

  <div class="sec-head" style="left:44px;top:822px;width:490px;font-size:11px;padding-top:6px">Latest news<span class="link" style="font-size:5px">Newsroom</span></div>

  <article class="news" style="left:44px">
    <div class="rule"></div>
    <h4 style="border:0">Former Hale &amp; Moss CEO Joins Varlo Finance Board Of Directors</h4>
    <div class="rule2"></div>
    <p>A key focus for the crowdfunding real estate investment company is to broaden its reach into institutional capital markets..</p>
    <span class="link green-link">Read more</span>
    <div class="pic" role="img" aria-label="Four executives standing together" style="background:linear-gradient(180deg,#d8d1c6,#8c7e70 60%,#3a3a40)"></div>
  </article>
  <article class="news" style="left:210px">
    <div class="rule"></div>
    <h4 style="border:0">How residential estate is puttin a new spin on fix-and-flip financing</h4>
    <div class="rule2"></div>
    <p>A key focus for the crowdfunding real estate investment company is to broaden its reach into institutional capital markets..</p>
    <span class="link green-link">Read more</span>
    <div class="pic" role="img" aria-label="Stone family house with a green lawn" style="background:linear-gradient(180deg,#7fb0d8,#8a7a68 45%,#6f9a3e 85%)"></div>
  </article>
  <article class="news" style="left:376px">
    <div class="rule"></div>
    <h4 style="border:0">Varlo Finance to fund over $9M in commercial debt next year</h4>
    <div class="rule2"></div>
    <p>A key focus for the crowdfunding real estate investment company is to broaden its reach into institutional capital markets..</p>
    <span class="link green-link">Read more</span>
    <div class="pic" role="img" aria-label="Modern commercial building facade" style="background:linear-gradient(180deg,#5e87b8,#c3ccd6 40%,#7b8591)"></div>
  </article>

  <div class="sec-head" style="left:44px;top:1005px;width:490px">Partners<span class="link">Investors</span></div>
  <div class="partners">
    <span>Coralwing</span><span>Dispatchly</span><span>Maple Choice</span><span>Cocoabar</span><span>Ardent Bank</span><span>Quillmark</span><span>Bullrun Capital</span>
  </div>

  <div class="abs footline"></div>
  <footer>
    <div class="foot-col" style="left:44px;width:60px"><h4>Loans</h4>Fix and Flip<br>Commercial Hard<br>Money</div>
    <div class="foot-col" style="left:110px"><h4>Investors</h4>Case studies<br>Projects</div>
    <div class="foot-col" style="left:169px"><h4>Borrowers</h4>Account<br>Transactions<br>Recent Projects<br>Vallue Add Services<br>Testimonials</div>
    <div class="foot-col" style="left:243px"><h4>Resources</h4>Blog<br>Industry News<br>Vallue Add Services<br>Testimonials</div>
    <div class="foot-col" style="left:309px"><h4>About</h4>Company<br>People<br>Blog<br>Newsroom</div>
    <div class="foot-col" style="left:434px"><h4>Contact</h4>info@varlofinance.example<br>1 (888) 555 0147<br>48 Alder Row, Fernbrook, PA, 32904</div>
    <div class="abs brand" style="left:44px;top:1166px;font-size:8px">Varlo Finance</div>
    <div class="abs legal" style="left:118px;top:1169px">Terms of Service &nbsp; Privacy Policy</div>
    <div class="abs legal" style="right:44px;top:1169px;color:var(--soft)">1 (888) 555 0190 — Our hours are weekdays 8am to 5pm</div>
  </footer>
</div>
</body>
</html>
```